Website R86 coffee

I am opening a small business selling locally roasted coffee online. To start with I want a site with three pages. 1. A welcome page with logo and mission/vision. 2. Shopping/ordering page. 3. About Us page. The brand is "R86 Coffee - A warm start to every day". We are giving back to the downs syndrome community by employing people with down syndrome (Trisomy 21) and buy donating to down syndrome research.

Target Market(s)

Families and friends of people with downs syndrome

Coding

Coded - Design and coding required

Number of Pages Required

3 page

```html
<!DOCTYPE html>
<html lang="en">
<head>
<meta charset="utf-8">
<title>R86 Coffee - A warm start to every day</title>
<link rel="stylesheet" href="https://fonts.googleapis.com/css2?family=Josefin+Sans:wght@300;400;600;700&family=Poppins:wght@300;400;500;600&display=swap">
<style>
:root{
  --bg:#262626;
  --header:#2b2b2b;
  --ink:#fff;
  --muted:#d6d6d6;
  --card:#ececec;
  --dark-text:#333;
  --price:#e0281e;
  --highlight:#555;
  --line:#f2f2f2;
}
*{box-sizing:border-box;margin:0;padding:0}
html,body{width:1200px;height:5124px;overflow:hidden}
body{position:relative;background:var(--bg);color:var(--ink);font-family:'Poppins',sans-serif;font-size:13px}
.abs{position:absolute}
.h-title{font-family:'Josefin Sans',sans-serif;font-weight:700;text-transform:uppercase;letter-spacing:.5px}
.btn{position:absolute;border:2px solid var(--line);color:var(--ink);font-size:12px;display:flex;align-items:center;justify-content:center}

/* brand name: plain text with one square */
.brand{position:absolute;display:flex;align-items:center;gap:10px;font-family:'Poppins',sans-serif;font-weight:500;color:var(--ink);white-space:nowrap}
.brand .dot{width:12px;height:12px;background:var(--ink);display:block}

/* header */
.site-header{left:0;top:0;width:1200px;height:152px;background:var(--header)}
.site-header .brand{left:74px;top:60px;font-size:22px}
.topbar{right:74px;top:34px;display:flex;gap:26px;align-items:center;font-size:11px}
.nav{right:74px;top:88px;display:flex;gap:22px;align-items:center;font-size:13px}
.nav a{color:var(--ink);text-decoration:none;padding:4px 6px}
.nav .active{border:1px solid #ddd}
.nav .pill{background:#eee;color:#333;border-radius:16px;padding:5px 18px}

/* hero */
.hero{left:0;top:152px;width:1200px;height:742px;background:linear-gradient(90deg,#3a3a3a,#2f2f2f 50%,#262626)}
.hero-photo{left:520px;top:0;width:680px;height:742px;background:radial-gradient(circle at 50% 52%,#6b3c1e 0,#4a2812 28%,#2e2e2e 52%,transparent 70%)}
.hero h1{left:74px;top:286px;font-size:42px;line-height:50px}
.hero p{left:74px;top:400px;width:400px;font-size:14px;line-height:17px;color:var(--muted)}
.hero .btn{left:74px;top:466px;width:168px;height:46px}
.slide-count{left:1114px;top:364px;font-size:12px}
.down{left:592px;top:716px}

/* vision mission */
.vm-brand{left:540px;top:1044px;width:124px;justify-content:center;font-size:18px}
.vision{left:200px;top:1014px;width:324px;text-align:right}
.vm-head{font-size:15px;font-weight:600;display:inline-flex;align-items:center;gap:8px}
.vision p{font-size:14px;line-height:17px;color:var(--muted);margin-top:10px}
.mission{left:682px;top:1006px;width:400px}
.mission p{font-size:11.5px;line-height:14px;color:var(--muted);margin-top:6px}

/* favourites */
.kicker{left:0;width:1200px;top:1200px;text-align:center;font-size:11px;letter-spacing:.3px}
.fav-title{left:0;width:1200px;top:1232px;text-align:center;font-size:33px}
.product{position:absolute;top:1296px;width:250px;height:432px;text-align:center}
.product.featured{background:var(--highlight)}
.product .shot{width:250px;height:330px}
.product .name{margin-top:20px;font-size:13px}
.product .price{margin-top:8px;font-size:12px;color:var(--price)}
.product .stars{margin-top:8px;font-size:11px;letter-spacing:1px}
.product .actions{position:absolute;top:292px;left:0;width:250px;display:flex;justify-content:center;gap:8px}
.product .actions span{width:28px;height:28px;border-radius:50%;border:1.5px solid #fff;background:rgba(0,0,0,.25)}

/* discount */
.discount{left:0;top:1878px;width:1200px;height:642px;background:linear-gradient(180deg,#8a7a4e,#a68a6a 40%,#cbb8a4 75%,#d9cfc4)}
.discount .frame{position:absolute;left:18px;top:18px;right:18px;bottom:18px;border:2px solid rgba(255,255,255,.8)}
.discount .k{left:0;width:1200px;top:270px;text-align:center;font-size:22px;font-family:'Josefin Sans',sans-serif;font-weight:300}
.discount .big{left:0;width:1200px;top:300px;text-align:center;font-size:42px;line-height:46px}
.discount .mid{left:0;width:1200px;top:354px;text-align:center;font-size:30px}
.discount .btn{left:516px;top:414px;width:168px;height:44px;font-size:11px}

/* about */
.about-title{left:0;width:1210px;top:2614px;text-align:center;font-size:33px}
.about-img{left:30px;top:2660px;width:540px;height:450px;background:radial-gradient(circle at 55% 45%,#d59a42 0,#b7732a 18%,#f3f3f3 34%,#e6e6e6 46%,transparent 58%)}
.badge{left:470px;top:2950px;width:118px;height:118px;border-radius:50%;background:#5a5a5a;border:5px solid #eee;text-align:center;padding-top:26px;font-family:'Josefin Sans',sans-serif;font-weight:700}
.badge b{font-size:42px;line-height:36px}
.badge small{font-size:11px}
.about-text{left:632px;top:2700px;width:460px;font-size:12px;line-height:22px;color:var(--muted)}
.about-text p{margin-bottom:22px}
.about-tabs{left:694px;top:2966px;font-size:15px;font-weight:600;display:flex;gap:124px}
.about .btn{left:632px;top:3024px;width:170px;height:46px}

/* clients */
.clients{left:0;top:3170px;width:1200px;height:365px;background:linear-gradient(90deg,#333,#2c2c2c 55%,#4a4643 80%,#3a3836)}
.clients .t{left:0;width:1216px;top:80px;text-align:center;font-size:25px}
.clients .q{left:380px;top:120px;width:460px;text-align:center;font-size:10.5px;line-height:13px}
.clients .who{left:0;width:1216px;top:208px;text-align:center;font-family:'Josefin Sans',sans-serif;font-size:23px}
.clients .rate{left:0;width:1210px;top:240px;text-align:center;color:#f4c400;font-size:14px;letter-spacing:1px}
.clients .dots{left:580px;top:266px;display:flex;gap:8px;align-items:center}
.clients .dots i{width:6px;height:6px;background:#fff;display:block}
.clients .dots i.on{width:10px;height:10px;background:none;border:1px solid #fff}
.clients .btn{left:528px;top:294px;width:146px;height:40px}

/* news */
.news-title{left:0;width:1214px;top:3618px;text-align:center;font-size:30px}
.news-card{position:absolute;top:3672px;width:318px;height:408px;background:var(--card);color:var(--dark-text);padding:10px}
.news-card .shot{width:298px;height:236px}
.news-card .date{position:absolute;left:30px;top:220px;width:38px;height:44px;background:#3a3a3a;color:#fff;font-size:11px;line-height:14px;text-align:center;padding-top:8px}
.news-card h3{font-weight:400;font-size:12.5px;margin:30px 10px 12px}
.news-card .rule{height:1px;background:#ccc;margin:0 10px 14px}
.news-card p{font-size:12px;line-height:14px;margin:0 10px;color:#555}
.news-card .arrow{margin:22px 10px 0}
.news .btn{left:516px;top:4122px;width:170px;height:44px}

.perk{position:absolute;top:4213px;width:308px;height:120px;border:2px solid #ddd;display:flex;align-items:center;gap:18px;padding-left:50px}
.perk b{display:block;font-size:16px;font-weight:600;letter-spacing:.5px}
.perk span{font-size:12px;line-height:14px;color:var(--muted)}

/* footer */
.footer{left:0;top:4370px;width:1200px;height:405px;background:linear-gradient(135deg,#2a2a2a,#1f1f1f 60%,#2b2b2b)}
.footer .brand{left:74px;top:136px;font-size:28px}
.socials{left:74px;top:254px;display:flex;gap:8px}
.socials i{width:28px;height:28px;border-radius:50%;border:2px solid #fff;display:block}
.fcol{position:absolute;top:86px;font-size:12.5px;line-height:22px;color:var(--muted)}
.fcol h4{font-size:13px;color:#fff;font-weight:500;margin-bottom:36px;letter-spacing:.3px}
.fcol li{list-style:none}
.fcol li::before{content:"\2192";margin-right:8px;font-size:10px}
.email{width:244px;height:32px;background:#fff;color:#777;font-style:italic;font-size:11px;padding:8px 16px;margin-top:18px}
.sub-btn{width:156px;height:34px;border:2px solid #fff;margin:12px 0 0 56px;text-align:center;line-height:30px;font-size:11px;color:#fff}
.bottom{left:0;top:4775px;width:1200px;height:44px;background:#1c1c1c}
.bottom .copy{left:74px;top:14px;font-size:12px}
.cards{right:74px;top:8px;display:flex;gap:8px}
.cards i{width:38px;height:26px;background:#e9e9e9;border-radius:2px;display:block}
</style>
</head>
<body>

<header class="abs site-header">
  <div class="brand"><i class="dot"></i>R86 Coffee</div>
  <div class="abs topbar">
    <span>&#9742; (00) 555 018 642</span>
    <svg width="14" height="14" viewBox="0 0 14 14" fill="none" stroke="#fff"><circle cx="7" cy="4.5" r="3"/><path d="M1.5 13c1-3 3-4.5 5.5-4.5S11.5 10 12.5 13"/></svg>
    <svg width="14" height="13" viewBox="0 0 14 13" fill="none" stroke="#fff"><path d="M7 12S1 8 1 4.2A3 3 0 0 1 7 3a3 3 0 0 1 6 1.2C13 8 7 12 7 12z"/></svg>
    <svg width="16" height="14" viewBox="0 0 16 14" fill="none" stroke="#fff"><path d="M1 1h2l2 8h8l2-6H4"/><circle cx="6" cy="12" r="1"/><circle cx="12" cy="12" r="1"/></svg>
    <svg width="16" height="12" viewBox="0 0 16 12" stroke="#fff" stroke-width="1.5"><path d="M0 1h16M0 6h16M0 11h16"/></svg>
  </div>
  <nav class="abs nav">
    <a class="active">Home</a><a>Shop</a><a>About us</a><a>News/Events</a><a>Contact us</a><a class="pill">Donating</a>
  </nav>
</header>

<section class="abs hero">
  <div class="abs hero-photo" role="img" aria-label="Bowl of roasted coffee beans with ground coffee and a green leaf on dark stone"></div>
  <h1 class="abs h-title">An essential part<br>of life</h1>
  <p class="abs">Lorem Ipsum is simply dummy text of the printing and typesetting industry.</p>
  <a class="btn">SHOP NOW</a>
  <div class="abs slide-count">02
    <svg class="abs" style="left:18px;top:-12px" width="40" height="36" stroke="#fff"><path d="M2 6h36M2 14h36M2 22h36M2 30h36"/></svg>
  </div>
  <svg class="abs down" width="16" height="22" fill="none" stroke="#fff"><path d="M8 0v20M3 15l5 5 5-5"/></svg>
</section>

<section class="vm">
  <div class="abs vision">
    <span class="vm-head">VISION
      <svg width="36" height="28" fill="none" stroke="#fff" stroke-width="1.5"><path d="M2 24l10-12 8 8 6-6 8 10"/><path d="M20 4v8M20 4l6 2-6 2"/></svg>
    </span>
    <p>Develop a company that markets coffee and related products to family and friends of the down syndrome community</p>
  </div>
  <div class="brand vm-brand">R86 Coffee</div>
  <div class="abs mission">
    <span class="vm-head">
      <svg width="30" height="30" fill="none" stroke="#fff" stroke-width="1.5"><circle cx="15" cy="15" r="12"/><circle cx="15" cy="15" r="7"/><circle cx="15" cy="15" r="2"/><path d="M15 15l12-12"/></svg>MISSION
    </span>
    <p>Create and grow an online company selling contract roasted coffee. As growth permits become a fully vertically integrated coffee company from roasting to our coffee shop. The company will give significant funds to medical research in downs syndrome and we will hire as many people with downs syndrome as possible.</p>
  </div>
</section>

<section class="favourites">
  <div class="abs kicker">WHAT HAPPENS HERE</div>
  <h2 class="abs h-title fav-title">Favourite Coffee Flavours</h2>
  <div class="product" style="left:74px">
    <div class="shot" role="img" aria-label="Dark roasted coffee beans" style="background:linear-gradient(135deg,#4a2a1c,#2a1810 50%,#5c3522)"></div>
    <div class="name">Roasted Coffee Beans</div><div class="price">$00.00</div><div class="stars">&#9733;&#9733;&#9733;&#9733;&#9733;</div>
  </div>
  <div class="product featured" style="left:342px">
    <div class="shot" role="img" aria-label="Medium brown dried coffee beans" style="background:linear-gradient(135deg,#8c5436,#6a3a24 50%,#9a6244)"></div>
    <div class="actions"><span></span><span></span><span></span></div>
    <div class="name">Dried Coffee Beans</div><div class="price">$00.00</div><div class="stars">&#9733;&#9733;&#9733;&#9733;&#9734;</div>
  </div>
  <div class="product" style="left:610px">
    <div class="shot" role="img" aria-label="Mixed dried coffee beans" style="background:linear-gradient(135deg,#5a3020,#3a1e12 50%,#6a3c28)"></div>
    <div class="name">Dried Coffee Beans</div><div class="price">$00.00</div><div class="stars">&#9733;&#9733;&#9733;&#9733;&#9733;</div>
  </div>
  <div class="product" style="left:878px">
    <div class="shot" role="img" aria-label="Green unroasted coffee beans" style="background:linear-gradient(135deg,#8aa83c,#6d8c2a 50%,#9cb84a)"></div>
    <div class="name">Green Coffee Beans</div><div class="price">$00.00</div><div class="stars">&#9733;&#9733;&#9733;&#9733;&#9733;</div>
  </div>
  <a class="btn" style="left:516px;top:1762px;width:170px;height:46px">View More</a>
</section>

<section class="abs discount" role="img" aria-label="Friends laughing over coffee cups and a phone at a café table">
  <div class="frame"></div>
  <div class="abs k">DISCOUNT OFFER</div>
  <div class="abs big h-title">Save 30% off</div>
  <div class="abs mid h-title">On your 1st oredr</div>
  <a class="btn">SHOP NOW</a>
</section>

<section class="about">
  <h2 class="abs h-title about-title">About Us</h2>
  <div class="abs about-img" role="img" aria-label="Latte with leaf art in a white cup beside coffee beans and leaves"></div>
  <div class="abs badge"><b>20</b><small>YEAR</small><br><small>EXPERIENCE</small></div>
  <div class="abs about-text">
    <p>Lorem Ipsum is simply dummy text of the printing and typesetting industry has been the industry's standard dummy text ever since the 1500s,</p>
    <p>when an unknown printer took a galley of type and scrambled it to make a type specimen book. It has survived not only five centuries, but also the leap into electronic typesetting, remaining essentially unchanged. It was popularised in the 1960s</p>
    <p>with the release of Letraset sheets containing Lorem Ipsum passages, and more recently with desktop publishing software</p>
  </div>
  <div class="abs about-tabs"><span>VISION</span><span>MISSION</span></div>
  <a class="btn">Read More</a>
</section>

<section class="abs clients" role="img" aria-label="Couple sharing coffee in a bright room">
  <h2 class="abs h-title t">Our Clients Say`s</h2>
  <svg class="abs" style="left:388px;top:94px" width="22" height="20" fill="#fff"><path d="M4 20L8 0h5L8 20zM12 20L16 0h5L16 20z"/></svg>
  <p class="abs q">Lorem Ipsum is simply dummy text of the printing and typesetting industry. Lorem Ipsum has been the industry's standard dummy text ever since the 1500s.</p>
  <svg class="abs" style="left:666px;top:180px" width="22" height="20" fill="#fff"><path d="M4 20L8 0h5L8 20zM12 20L16 0h5L16 20z"/></svg>
  <div class="abs who">MARA LINDEN</div>
  <div class="abs rate">&#9733;&#9733;&#9733;&#9733;&#9733;</div>
  <div class="abs dots"><i class="on"></i><i></i><i></i></div>
  <a class="btn">BROWS MORE</a>
</section>

<section class="news">
  <h2 class="abs h-title news-title">News/Events</h2>
  <article class="news-card" style="left:104px">
    <div class="shot" role="img" aria-label="Child playing with a stacking toy" style="background:linear-gradient(160deg,#9bb6c8,#d8c2a8 60%,#7a5a4a)"></div>
    <div class="date">02<br>Sep</div>
    <h3>Blog Heading 01</h3><div class="rule"></div>
    <p>Lorem Ipsum is simply next dummy text of printing and typesetting industry...</p>
    <div class="arrow">&#10230;</div>
  </article>
  <article class="news-card" style="left:440px">
    <div class="shot" role="img" aria-label="Group of smiling children outdoors" style="background:linear-gradient(160deg,#a8b89a,#c98a8a 55%,#6a4a5a)"></div>
    <div class="date">02<br>Sep</div>
    <h3>Blog Heading 01</h3><div class="rule"></div>
    <p>Lorem Ipsum is simply next dummy text of printing and typesetting industry...</p>
    <div class="arrow">&#10230;</div>
  </article>
  <article class="news-card" style="left:776px">
    <div class="shot" role="img" aria-label="Doctor checking a child's blood pressure" style="background:linear-gradient(160deg,#e8eef2,#c8d2da 55%,#8a9aa6)"></div>
    <div class="date">02<br>Sep</div>
    <h3>Blog Heading 01</h3><div class="rule"></div>
    <p>Lorem Ipsum is simply next dummy text of printing and typesetting industry...</p>
    <div class="arrow">&#10230;</div>
  </article>
  <a class="btn">View More</a>

  <div class="perk" style="left:114px">
    <svg width="58" height="58" fill="none" stroke="#fff" stroke-width="1.5"><circle cx="29" cy="29" r="24"/><path d="M5 29h48M29 5v48M12 12l34 34"/></svg>
    <div><b>Free Delivery</b><span>Delivery On All Orders<br>Over $100</span></div>
  </div>
  <div class="perk" style="left:450px">
    <svg width="58" height="58" fill="none" stroke="#fff" stroke-width="1.5"><circle cx="26" cy="24" r="16"/><path d="M19 31l14-14"/><circle cx="20" cy="18" r="2.5"/><circle cx="32" cy="30" r="2.5"/><path d="M6 50c6-6 14-8 24-6l14-6"/></svg>
    <div><b>Sale &amp; Discounts</b><span>Get Personalized Offer<br>Every Week</span></div>
  </div>
  <div class="perk" style="left:784px">
    <svg width="58" height="58" fill="none" stroke="#fff" stroke-width="1.5"><circle cx="30" cy="30" r="22"/><path d="M8 30a22 22 0 0 1 6-15l4 4"/><text x="19" y="34" fill="#fff" stroke="none" font-size="11" font-family="Poppins">24/7</text></svg>
    <div><b>Service Online</b><span>You Can Pay Online<br>Or Courier</span></div>
  </div>
</section>

<footer class="abs footer">
  <div class="brand"><i class="dot"></i>R86 Coffee</div>
  <div class="abs socials"><i></i><i></i><i></i><i></i></div>
  <div class="fcol" style="left:414px">
    <h4>QUICK LINK</h4>
    <ul><li>Home</li><li>Shop</li><li>About us</li><li>News/Events</li><li>Contact us</li><li>Donating</li></ul>
  </div>
  <div class="fcol" style="left:632px">
    <h4>ADDRESS</h4>
    <div>&#9679;&nbsp;&nbsp; 48 Roastery Lane<br>&nbsp;&nbsp;&nbsp;&nbsp;&nbsp; Millbrook, USA<br>&nbsp;&nbsp;&nbsp;&nbsp;&nbsp; Zip :40861</div>
    <div style="margin-top:20px">&#9742;&nbsp; +100 555 0186<br>&#9993;&nbsp; hello@r86coffee.com</div>
  </div>
  <div class="fcol" style="left:880px;width:250px">
    <h4>NEWSLETTER</h4>
    <div style="line-height:14px;font-size:12px;margin-top:-20px">Lorem Ipsum is simply next dummy text printing and typesetting industry...</div>
    <div class="email">Email Address</div>
    <div class="sub-btn">SUBSCRIBE</div>
  </div>
</footer>

<div class="abs bottom">
  <div class="abs copy">Copyright © 2021 <b>R86 COFFEE</b>, All Rights Reserved.</div>
  <div class="abs cards"><i></i><i></i><i></i><i></i></div>
</div>

</body>
</html>
```